Velvor IT Services Business Card

Velvor IT Services are a Perth based IT Services company. We would like to incorporate our company logo (attached) and stick with the blue that is in that design. I would like a clean look design that isn't too busy, yet creates a lasting image that is instantly recognisable in the recipients mind.

Target Market(s)

The target audience is small/medium business owners.

Industry/Entity Type

Business

Font styles to use
Serif
Sans Serif

Colors

Designer to choose colors to be used in the design.

Requirements
Must have
• The design should include:
Business name: Velvor IT Services
Directors Name: Marcus Dredge
Phone Number: 0483 906 452
Email: support@velvorit.com.au
Website: www.velvorit.com.au

```html
<!DOCTYPE html>
<html lang="en">
<head>
<meta charset="utf-8">
<title>Velvor IT Services – Business Card</title>
<link rel="stylesheet" href="https://fonts.googleapis.com/css2?family=Oswald:wght@400;500&family=Roboto+Condensed:wght@400&display=swap">
<style>
  :root {
    --stage: #3b3b3e;
    --front-light: #ffffff;
    --front-edge: #d4d4d6;
    --brand-blue: #1f5cb3;
    --back-left: #1b4eae;
    --back-right: #0b73ba;
    --ink-light: #ffffff;
  }
  * { margin: 0; padding: 0; box-sizing: border-box; }
  html, body { width: 1031px; height: 1200px; overflow: hidden; }
  body {
    background: var(--stage);
    position: relative;
    font-family: "Oswald", sans-serif;
  }
  .card {
    position: absolute;
    left: 155px;
    width: 720px;
    height: 433px;
  }
  .card-front {
    top: 123px;
    background: radial-gradient(ellipse at 50% 45%, var(--front-light) 0%, #f1f1f2 45%, var(--front-edge) 100%);
  }
  .card-back {
    top: 655px;
    background: linear-gradient(90deg, var(--back-left) 0%, var(--back-right) 100%);
    color: var(--ink-light);
  }
  .wordmark {
    position: absolute;
    font-family: "Oswald", sans-serif;
    font-weight: 500;
    text-transform: uppercase;
    line-height: 1;
  }
  .wordmark .name { display: block; font-size: 48px; letter-spacing: 1px; }
  .wordmark .tag { display: block; font-size: 13px; letter-spacing: 9px; margin-top: 4px; }
  .card-front .wordmark { left: 0; right: 0; top: 168px; text-align: center; color: var(--brand-blue); }
  .card-back .wordmark { left: 60px; top: 118px; color: var(--ink-light); }
  .holder {
    position: absolute;
    left: 44px;
    top: 325px;
  }
  .holder-name {
    font-family: "Oswald", sans-serif;
    font-weight: 400;
    font-size: 31px;
    letter-spacing: 0.5px;
    text-transform: uppercase;
    line-height: 1;
  }
  .holder-role {
    font-family: "Roboto Condensed", sans-serif;
    font-size: 15px;
    margin-top: 6px;
  }
  .contact {
    position: absolute;
    left: 441px;
    top: 321px;
    list-style: none;
    font-family: "Roboto Condensed", sans-serif;
    font-size: 18px;
    line-height: 26px;
  }
  .contact b { font-family: "Oswald", sans-serif; font-weight: 500; margin-right: 3px; }
</style>
</head>
<body>
  <section class="card card-front">
    <div class="wordmark">
      <span class="name">Velvor</span>
      <span class="tag">IT Services</span>
    </div>
  </section>

  <section class="card card-back">
    <div class="wordmark">
      <span class="name">Velvor</span>
      <span class="tag">IT Services</span>
    </div>
    <div class="holder">
      <p class="holder-name">Marcus Dredge</p>
      <p class="holder-role">director</p>
    </div>
    <ul class="contact">
      <li><b>P:</b>0483 906 452</li>
      <li><b>E:</b>support@velvorit.com.au</li>
      <li><b>W:</b>www.velvorit.com.au</li>
    </ul>
  </section>
</body>
</html>
```